LumaVantix
stationery - business cards
LumaVantix -
Creative Brief
Professional
Carl MORVEDO
41 Pellin Lane, suite 218 San Mateo, California, 94402
cm@lumavantix.com
www.lumavantix.com
Free to be creative

```html
<!DOCTYPE html>
<html lang="en">
<head>
<meta charset="utf-8">
<title>LumaVantix Stationery</title>
<link rel="stylesheet" href="https://fonts.googleapis.com/css2?family=Open+Sans:wght@400;600;700&display=swap">
<style>
  :root {
    --brand-blue: #2f5aa8;
    --brand-blue-dark: #1f4390;
    --brand-blue-light: #4a78c4;
    --ink: #333a44;
    --paper: #ffffff;
    --hairline: #c9cfd8;
    --canvas: #ffffff;
  }
  * { box-sizing: border-box; margin: 0; padding: 0; }
  html, body { width: 1200px; height: 701px; overflow: hidden; background: var(--canvas); }
  body { font-family: "Open Sans", Arial, sans-serif; color: var(--ink); position: relative; }

  .sheet { position: absolute; background: var(--paper); box-shadow: 0 0 0 1px var(--hairline); overflow: hidden; }

  .side-strip {
    position: absolute; left: 0; top: 0; bottom: 0;
    background: linear-gradient(90deg, var(--brand-blue-dark), var(--brand-blue-light));
  }
  .mark-square { position: absolute; background: #fff; border-radius: 2px; }

  .wordmark { position: absolute; display: flex; align-items: center; gap: 6px; color: var(--brand-blue); font-weight: 700; white-space: nowrap; }
  .wordmark .mark-dot { background: var(--brand-blue); border-radius: 2px; flex: none; }

  /* Business card front */
  .card-front { left: 38px; top: 84px; width: 262px; height: 127px; }
  .card-front .side-strip { width: 17px; }
  .card-front .mark-square { left: 4px; top: 57px; width: 9px; height: 9px; }
  .card-front .wordmark { right: 10px; top: 8px; font-size: 10px; gap: 4px; }
  .card-front .wordmark .mark-dot { width: 9px; height: 9px; }
  .card-holder { position: absolute; left: 48px; top: 46px; font-size: 11px; font-weight: 700; color: var(--brand-blue); }
  .card-details { position: absolute; left: 48px; top: 66px; font-size: 5.5px; line-height: 9px; }
  .card-details .label { font-weight: 700; color: var(--brand-blue); }

  /* Business card back */
  .card-back {
    left: 360px; top: 84px; width: 262px; height: 127px;
    background: radial-gradient(ellipse at 50% 40%, var(--brand-blue-light), var(--brand-blue-dark));
    box-shadow: none;
  }
  .card-back .mark-square { left: 119px; top: 36px; width: 24px; height: 24px; border-radius: 3px; }
  .card-back .web { position: absolute; left: 0; right: 0; top: 86px; text-align: center; font-size: 6px; color: #fff; }

  /* Envelope */
  .envelope { left: 24px; top: 276px; width: 605px; height: 408px; border-radius: 30px 30px 0 0; background: var(--brand-blue); box-shadow: none; }
  .envelope .flap-text { position: absolute; left: 0; right: 0; top: 26px; text-align: center; font-size: 6px; color: #fff; }
  .envelope .flap-square { left: 296px; top: 44px; width: 13px; height: 13px; }
  .envelope .body {
    position: absolute; left: 0; right: 0; top: 84px; bottom: 0;
    background: var(--paper);
    box-shadow: inset 0 0 0 1px var(--hairline);
  }
  .envelope .side-strip { top: 84px; width: 26px; }
  .envelope .strip-square { left: 7px; top: 236px; width: 13px; height: 13px; }
  .envelope .wordmark { left: 34px; top: 100px; font-size: 22px; }
  .envelope .wordmark .mark-dot { width: 20px; height: 20px; }
  .envelope .address { position: absolute; left: 46px; bottom: 10px; font-size: 9px; line-height: 12px; }
  .envelope .address .accent { color: var(--brand-blue); }

  /* Letterhead */
  .letterhead { left: 682px; top: 19px; width: 508px; height: 670px; }
  .letterhead .side-strip { width: 40px; }
  .letterhead .mark-square { left: 13px; top: 336px; width: 14px; height: 14px; }
  .letterhead .wordmark { left: 58px; top: 24px; font-size: 22px; }
  .letterhead .wordmark .mark-dot { width: 20px; height: 20px; }
  .letterhead .address { position: absolute; right: 12px; top: 18px; text-align: right; font-size: 9.5px; line-height: 13px; }
  .letterhead .address .accent { color: var(--brand-blue); }
</style>
</head>
<body>

  <section class="sheet card-front" aria-label="Business card front">
    <div class="side-strip"></div>
    <span class="mark-square"></span>
    <div class="wordmark"><span class="mark-dot"></span>LumaVantix</div>
    <p class="card-holder">Carl MORVEDO</p>
    <div class="card-details">
      <p>41 Pellin Lane, suite 218</p>
      <p>Corvella Bay, Oregon, 97031</p>
      <p><span class="label">Phone:</span> (541) 555 0162</p>
      <p><span class="label">Email:</span> cm@lumavantix.com</p>
    </div>
  </section>

  <section class="sheet card-back" aria-label="Business card back">
    <span class="mark-square"></span>
    <p class="web">www.lumavantix.com</p>
  </section>

  <section class="sheet envelope" aria-label="Envelope">
    <p class="flap-text">www.lumavantix.com</p>
    <span class="mark-square flap-square"></span>
    <div class="body"></div>
    <div class="side-strip"></div>
    <span class="mark-square strip-square"></span>
    <div class="wordmark"><span class="mark-dot"></span>LumaVantix</div>
    <div class="address">
      <p>41 Pellin Lane, suite 218</p>
      <p>Corvella Bay, Oregon, 97031</p>
      <p class="accent">Phone: (541) 555 0162</p>
      <p class="accent">Email: cm@lumavantix.com</p>
    </div>
  </section>

  <section class="sheet letterhead" aria-label="Letterhead">
    <div class="side-strip"></div>
    <span class="mark-square"></span>
    <div class="wordmark"><span class="mark-dot"></span>LumaVantix</div>
    <div class="address">
      <p>41 Pellin Lane, suite 218</p>
      <p>Corvella Bay, Oregon, 97031</p>
      <p class="accent">Phone: (541) 555 0162</p>
    </div>
  </section>

</body>
</html>
```